Visitenkarten-Design für K17.eu - TradeWing Finanz
Zielgruppe
Smartphone-Banking mit Mehrwert
Aufgabenstellung
Bitte entwerfen Sie kreative Visitenkarten für uns.
- Halten Sie einen Platz/Rahmen frei für Fotos, die wir nachträglich einsetzen, und kennzeichnen diesen.
- Halten Sie einen Patz/Rahmen für Vor- und Nachname sowie für die Berufsbezeichnung frei und kennzeichnen diesen.
- Halten Sie einen Platz/Rahmen für die Telefonnummern und die Email-Adressen frei und kennzeichnen diesen.
Alle Visitenkarten sollen folgende Daten beinhalten:
Vorname Nachname*
Berufsbezeichnung*
Mobile:
Office:
Email:
Domain:
* = individuell, jeder Mitarbeiter hat eigene Daten
Die Farben müssen sich an unserem CI-Design orientieren, orange/weiß/schwarz/grau -
Außerdem finden Sie unser Logo in der Anlage, welches Sie bitte auf der Karte platzieren.
Bitte liefern Sie uns die Designs in verschiedenen Formaten - psd, ai, eps, jpg, png
Bei Fragen zögern Sie nicht, uns zu kontaktieren. Danke.

```html
<!DOCTYPE html>
<html lang="de">
<head>
<meta charset="utf-8">
<title>K17.eu – Visitenkarte</title>
<link rel="stylesheet" href="https://fonts.googleapis.com/css2?family=Roboto:wght@400;500;700&display=swap">
<style>
  :root {
    --bg: #e4e4e4;
    --paper: #f7f6f3;
    --orange: #e8622a;
    --orange-light: #f07a3e;
    --orange-dark: #d2501d;
    --charcoal: #4a4a4a;
    --grey-band: #6b6b6b;
    --text-grey: #555555;
    --white: #ffffff;
  }
  * { box-sizing: border-box; margin: 0; padding: 0; }
  html, body { width: 1200px; height: 900px; overflow: hidden; }
  body {
    background: var(--bg);
    font-family: "Roboto", Arial, sans-serif;
    display: flex;
    flex-direction: column;
    align-items: center;
    justify-content: center;
    gap: 40px;
  }
  .card {
    width: 660px;
    height: 380px;
    background: var(--paper);
    position: relative;
    overflow: hidden;
    box-shadow: 0 6px 18px rgba(0,0,0,0.18);
  }
  /* Back side */
  .card--back { display: flex; align-items: center; justify-content: center; }
  .wordmark { display: flex; align-items: center; gap: 14px; }
  .wordmark__square { width: 34px; height: 34px; background: var(--orange); }
  .wordmark__name { font-weight: 700; font-size: 54px; color: var(--charcoal); letter-spacing: 1px; }
  .card--back .wordmark__name { font-size: 62px; }
  /* Front side */
  .front__brand { position: absolute; left: 40px; top: 175px; }
  .front__brand .wordmark__name { font-size: 46px; }
  .front__brand .wordmark__square { width: 28px; height: 28px; }
  .address { margin-top: 14px; font-size: 21px; line-height: 1.15; color: var(--text-grey); }
  .front__panel {
    position: absolute; right: 0; top: 0; width: 290px; height: 100%;
    background: linear-gradient(200deg, var(--orange-light) 0%, var(--orange) 55%, var(--orange-dark) 100%);
  }
  .name-band {
    position: absolute; left: 330px; top: 60px; width: 330px; height: 62px;
    background: var(--grey-band);
    padding: 6px 0 0 78px;
    color: var(--white);
  }
  .name-band__name { font-size: 30px; font-weight: 400; line-height: 1; }
  .name-band__title { font-size: 11px; letter-spacing: 2px; margin-top: 4px; text-align: right; padding-right: 120px; }
  .photo-slot {
    position: absolute; left: 270px; top: 25px; width: 140px; height: 140px;
    border-radius: 50%;
    border: 4px solid var(--white);
    background: radial-gradient(circle at 50% 40%, #8a8a8a, #3a3a3a);
  }
  .contact {
    position: absolute; left: 410px; top: 175px;
    color: var(--white); font-size: 14px; line-height: 1.45;
    border-collapse: collapse;
  }
  .contact th { text-align: left; font-weight: 700; padding-right: 8px; }
  .contact td { font-weight: 400; }
</style>
</head>
<body>
  <section class="card card--back" aria-label="Kartenrückseite">
    <div class="wordmark">
      <span class="wordmark__square"></span>
      <span class="wordmark__name">K17.eu</span>
    </div>
  </section>

  <section class="card card--front" aria-label="Kartenvorderseite">
    <div class="front__panel"></div>
    <div class="name-band">
      <div class="name-band__name">Yourname</div>
      <div class="name-band__title">JOB TITLE</div>
    </div>
    <div class="photo-slot" role="img" aria-label="Platzhalter für Mitarbeiterfoto"></div>
    <div class="front__brand">
      <div class="wordmark">
        <span class="wordmark__square"></span>
        <span class="wordmark__name">K17.eu</span>
      </div>
      <p class="address">Lindenweg 9<br>84028 Landshut<br>Germany</p>
    </div>
    <table class="contact">
      <tr><th>Mobile</th><td>: +49 160 0000000</td></tr>
      <tr><th>Office</th><td>: +49 871 000000-00</td></tr>
      <tr><th>Email</th><td>: yourname@k17.eu</td></tr>
      <tr><th>Domain</th><td>: www.k17.eu</td></tr>
    </table>
  </section>
</body>
</html>
```